2021 Summer Ads Danford Vale Custom Homes

We need a re-design of our summer ad run for our customer, Danford Vale Custom Homes. They are custom home builders in the mostly rural parts of West Virginia, USA. They are known for their "Forever Home" tagline. We'd like two designed ads with the main difference being just the custom home that's featured. These designs should be for a Google banner like 300 x 250 and square ad like 250 x 250. For inspiration please visit the Danford Vale Custom Homes website at www dot danfordvalecustomhomes dot com

Target Market(s)

consumers / new home shoppers

Industry/Entity Type

Consumer

Requirements
Must have
• DVCH logo
Price Lock Available!
Custom home pic
Learn more >
small TBWG logo mark

```html
<!DOCTYPE html>
<html lang="en">
<head>
<meta charset="utf-8">
<title>Danford Vale Custom Homes – Summer Ads</title>
<link rel="stylesheet" href="https://fonts.googleapis.com/css2?family=Montserrat:wght@500;700;800&family=Oswald:wght@600&family=Great+Vibes&display=swap">
<style>
  :root {
    --board: #6b6b70;
    --red: #d3141b;
    --red-deep: #9e0a10;
    --white: #ffffff;
    --ink: #1d1d1d;
    --black: #0d0d0d;
  }
  * { box-sizing: border-box; margin: 0; padding: 0; }
  html, body { width: 1200px; height: 1200px; overflow: hidden; }
  body { background: var(--board); position: relative; font-family: "Montserrat", sans-serif; }

  .ad { position: absolute; width: 615px; height: 512px; overflow: hidden; box-shadow: 0 4px 14px rgba(0,0,0,.35); }
  .ad--light { left: 190px; top: 70px; background: var(--white); }
  .ad--dark { left: 406px; top: 625px; background: var(--black); }

  .ad__photo { position: absolute; left: 0; top: 0; width: 615px; height: 400px; }
  .ad--light .ad__photo {
    background: linear-gradient(180deg, #8fb6df 0%, #b9cfe2 14%, #4f7a3a 30%, #e9e7e2 46%, #d9d5cf 62%, #8e8377 78%, #6f8a3c 100%);
  }
  .ad--dark .ad__photo {
    background: linear-gradient(180deg, #cfdbe8 0%, #5e7c45 14%, #3f5f2f 42%, #b5262a 58%, #efece6 70%, #c9bfae 86%, #8c8276 100%);
  }
  .ad__shapes { position: absolute; left: 0; top: 0; width: 615px; height: 512px; }

  .partner-mark { position: absolute; left: 14px; top: 10px; width: 58px; height: 58px; border-radius: 50%; background: var(--white); border: 3px solid var(--red); }
  .ad--light .partner-mark { left: 12px; top: 8px; width: 44px; height: 44px; border-color: #1f3f8f; }

  .price-badge { position: absolute; left: 512px; top: 293px; width: 80px; height: 80px; border-radius: 50%; display: flex; align-items: center; justify-content: center; text-align: center; font-weight: 800; font-size: 10.5px; line-height: 1.2; letter-spacing: .2px; }
  .ad--light .price-badge { background: var(--red); color: var(--white); box-shadow: inset 0 0 0 4px var(--red), inset 0 0 0 6px var(--white), 0 3px 6px rgba(0,0,0,.3); }
  .ad--dark .price-badge { left: 492px; top: 285px; background: var(--white); color: var(--red); box-shadow: inset 0 0 0 4px var(--white), inset 0 0 0 6px var(--red), 0 3px 6px rgba(0,0,0,.3); }

  .brand-seal { position: absolute; left: 2px; top: 344px; width: 204px; height: 204px; border-radius: 50%; background: var(--white); border: 4px solid var(--red); display: flex; justify-content: center; padding-top: 58px; }
  .brand-seal__name { font-weight: 700; font-size: 17px; line-height: 1.15; color: var(--red); text-align: center; width: 150px; }

  .headline { position: absolute; left: 230px; top: 384px; }
  .headline__lead { display: block; font-weight: 500; font-size: 23px; line-height: 1; color: var(--ink); }
  .headline__main { display: block; margin-top: 4px; white-space: nowrap; }
  .headline__forever { font-family: "Oswald", sans-serif; font-weight: 600; font-size: 42px; line-height: 1; color: var(--red); letter-spacing: .3px; }
  .headline__today { font-family: "Great Vibes", cursive; font-size: 34px; color: var(--ink); margin-left: 4px; }
  .ad--dark .headline__lead,
  .ad--dark .headline__forever,
  .ad--dark .headline__today { color: var(--white); }

  .cta { position: absolute; left: 224px; top: 468px; width: 256px; height: 38px; display: flex; align-items: center; padding-left: 46px; gap: 10px; color: var(--white); font-weight: 700; font-size: 20px; }
  .ad--dark .cta { top: 467px; }
  .cta__shape { position: absolute; left: 0; top: 0; width: 256px; height: 38px; z-index: 0; }
  .cta__label, .cta__arrow { position: relative; z-index: 1; }
</style>
</head>
<body>

  <section class="ad ad--light" aria-label="Square ad – barn-style custom home">
    <div class="ad__photo" role="img" aria-label="Photo of a white board-and-batten custom home with stone base, double garage and landscaped garden"></div>
    <svg class="ad__shapes" viewBox="0 0 615 512" aria-hidden="true">
      <path d="M0 336 Q300 372 615 292 L615 512 L0 512 Z" fill="var(--red-deep)"/>
      <path d="M0 344 Q300 380 615 306 L615 512 L0 512 Z" fill="var(--red)"/>
      <path d="M0 350 Q320 392 615 322 L615 512 L0 512 Z" fill="var(--white)"/>
      <rect x="0" y="505" width="615" height="7" fill="var(--red)"/>
    </svg>
    <div class="partner-mark"></div>
    <div class="price-badge">PRICE<br>LOCK<br>AVAILABLE</div>
    <div class="headline">
      <span class="headline__lead">Start Building Your</span>
      <span class="headline__main"><span class="headline__forever">FOREVER HOME</span><span class="headline__today">Today!</span></span>
    </div>
    <a class="cta">
      <svg class="cta__shape" viewBox="0 0 256 38" aria-hidden="true"><path d="M0 38 Q14 0 40 0 L236 0 Q256 0 250 19 Q244 38 226 38 Z" fill="var(--red)"/></svg>
      <span class="cta__label">Learn More</span>
      <svg class="cta__arrow" width="20" height="20" viewBox="0 0 20 20" aria-hidden="true"><circle cx="10" cy="10" r="10" fill="var(--white)"/><path d="M8 5 L13 10 L8 15" fill="none" stroke="var(--red)" stroke-width="3" stroke-linecap="round" stroke-linejoin="round"/></svg>
    </a>
    <div class="brand-seal"><span class="brand-seal__name">Danford Vale<br>Custom Homes</span></div>
  </section>

  <section class="ad ad--dark" aria-label="Banner ad – red barn garage custom home">
    <div class="ad__photo" role="img" aria-label="Photo of a white ranch home joined to a red board-and-batten garage with cupola, set against tall trees"></div>
    <svg class="ad__shapes" viewBox="0 0 615 512" aria-hidden="true">
      <path d="M0 292 Q260 370 615 292 L615 512 L0 512 Z" fill="var(--red)"/>
      <path d="M0 306 Q270 384 615 310 L615 512 L0 512 Z" fill="var(--white)"/>
      <path d="M0 316 Q280 392 615 324 L615 512 L0 512 Z" fill="var(--red)"/>
      <path d="M0 326 Q290 402 615 338 L615 512 L0 512 Z" fill="var(--black)"/>
      <rect x="0" y="505" width="615" height="7" fill="var(--red)"/>
    </svg>
    <div class="partner-mark"></div>
    <div class="price-badge">PRICE<br>LOCK<br>AVAILABLE</div>
    <div class="headline">
      <span class="headline__lead">Start Building Your</span>
      <span class="headline__main"><span class="headline__forever">FOREVER HOME</span><span class="headline__today">Today!</span></span>
    </div>
    <a class="cta">
      <svg class="cta__shape" viewBox="0 0 256 38" aria-hidden="true"><path d="M0 38 Q14 0 40 0 L236 0 Q256 0 250 19 Q244 38 226 38 Z" fill="var(--red)"/></svg>
      <span class="cta__label">Learn More</span>
      <svg class="cta__arrow" width="20" height="20" viewBox="0 0 20 20" aria-hidden="true"><circle cx="10" cy="10" r="10" fill="var(--white)"/><path d="M8 5 L13 10 L8 15" fill="none" stroke="var(--red)" stroke-width="3" stroke-linecap="round" stroke-linejoin="round"/></svg>
    </a>
    <div class="brand-seal"><span class="brand-seal__name">Danford Vale<br>Custom Homes</span></div>
  </section>

</body>
</html>
```